Business Card Design for Small Electrical Contractor

I need to update my business card into something a little more modern. We are a small electrical contracting company. We service domestic and commercial places around Sydney. We have 2 logo designs at the moment. I have uploaded both and 2 different sizes to work with.

Industry/Entity Type

Business

Contact Information for Business Card

Leo Hartigan
8/21-23 Birch Rd, Kelsworth 2087
t - (02) 9381 4720
m - 0427 815 903
E - info@hartiganelx.com.au
W - hartiganelx.com.au
ABN: 42 907 551 316

Font styles to use
Sans Serif

Requirements
Must have
• I would also like to see the below fit on somewhere aswell
• - Licensed Electrician
• - Level 2 (Cat 1 & 4)
• - Domestic
• - Commercial
• - Repairs and Installations
• - Data
Nice to have
• Try and keep similar colours as logo
Should not have
• No lightning bolts or light globes. Smart and professional please.

```html
<!DOCTYPE html>
<html lang="en">
<head>
<meta charset="utf-8">
<title>Hartigan Electrical – Business Card</title>
<link href="https://fonts.googleapis.com/css2?family=Questrial&family=Libre+Baskerville:wght@400;700&display=swap" rel="stylesheet">
<style>
  :root {
    --page: #e9e7e4;
    --amber: #efa934;
    --steel: #9c9c9c;
    --steel-light: #c4c4c4;
    --ink: #2b3434;
    --card-edge: #f4f4f4;
  }
  * { margin: 0; padding: 0; box-sizing: border-box; }
  html, body {
    width: 1200px;
    height: 1035px;
    overflow: hidden;
    background: var(--page);
  }
  .card {
    position: absolute;
    left: 190px;
    width: 820px;
    height: 469px;
    background: var(--card-edge);
    box-shadow: 0 6px 18px rgba(0,0,0,0.18);
  }
  .card--back { top: 36px; }
  .card--front { top: 530px; }
  .card__frame {
    position: absolute;
    inset: 0;
    width: 100%;
    height: 100%;
  }
  .card__content {
    position: absolute;
    inset: 0;
    color: var(--ink);
    font-family: "Questrial", sans-serif;
  }

  /* contact side */
  .holder {
    position: absolute;
    left: 100px;
    top: 62px;
    line-height: 1;
  }
  .holder__first {
    font-family: "Libre Baskerville", serif;
    font-weight: 700;
    font-size: 74px;
    letter-spacing: -1px;
  }
  .holder__last {
    font-family: "Libre Baskerville", serif;
    font-size: 22px;
    letter-spacing: 3px;
    margin-top: -6px;
  }
  .phones {
    position: absolute;
    left: 440px;
    top: 98px;
    list-style: none;
  }
  .details {
    position: absolute;
    left: 100px;
    top: 196px;
    list-style: none;
  }
  .contact-line {
    display: flex;
    align-items: center;
    gap: 14px;
    font-size: 27px;
    height: 42px;
    white-space: nowrap;
  }
  .icon {
    width: 26px;
    height: 26px;
    flex: none;
  }

  /* name side */
  .brand {
    position: absolute;
    left: 60px;
    right: 60px;
    top: 56px;
    bottom: 56px;
    display: flex;
    flex-direction: column;
    align-items: center;
    justify-content: center;
    gap: 30px;
  }
  .brand__title {
    display: flex;
    align-items: center;
    gap: 20px;
  }
  .brand__mark {
    width: 30px;
    height: 30px;
    background: var(--amber);
  }
  .brand__name {
    font-size: 60px;
    color: var(--ink);
    white-space: nowrap;
  }
  .services {
    list-style: none;
    text-align: center;
    font-size: 21px;
    line-height: 1.5;
    color: var(--ink);
    border-top: 2px solid var(--amber);
    padding-top: 16px;
    width: 600px;
  }
  .services__row { white-space: nowrap; }
  .services__sep { color: var(--amber); padding: 0 8px; }
</style>
</head>
<body>

<section class="card card--back" aria-label="Business card, contact side">
  <svg class="card__frame" viewBox="0 0 820 469" aria-hidden="true">
    <defs>
      <linearGradient id="panelBack" x1="0" y1="0" x2="0.3" y2="1">
        <stop offset="0" stop-color="#f8f8f8"/>
        <stop offset="1" stop-color="#c6c6c6"/>
      </linearGradient>
    </defs>
    <rect x="14" y="14" width="792" height="441" fill="var(--amber)"/>
    <rect x="14" y="14" width="470" height="14" fill="var(--steel-light)"/>
    <rect x="770" y="200" width="36" height="255" fill="var(--steel)"/>
    <rect x="300" y="426" width="506" height="29" fill="var(--steel)"/>
    <rect x="60" y="44" width="710" height="370" fill="url(#panelBack)"/>
  </svg>
  <div class="card__content">
    <div class="holder">
      <div class="holder__first">leo</div>
      <div class="holder__last">HARTIGAN</div>
    </div>
    <ul class="phones">
      <li class="contact-line">
        <svg class="icon" viewBox="0 0 26 26" aria-label="Phone"><rect width="26" height="26" rx="4" fill="var(--ink)"/><path d="M8 6l3 0 1 4-2 1.5c1 2 2.5 3.5 4.5 4.5L16 14l4 1v3c0 1-1 2-2 2C11 19 7 15 6 8c0-1 1-2 2-2z" fill="#fff"/></svg>
        <span>(02) 9381 4720</span>
      </li>
      <li class="contact-line">
        <svg class="icon" viewBox="0 0 26 26" aria-label="Mobile"><rect width="26" height="26" rx="4" fill="var(--ink)"/><rect x="8" y="4" width="10" height="18" rx="2" fill="#fff"/><rect x="10" y="7" width="6" height="10" fill="var(--ink)"/></svg>
        <span>0427 815 903</span>
      </li>
    </ul>
    <ul class="details">
      <li class="contact-line">
        <svg class="icon" viewBox="0 0 26 26" aria-label="Address"><rect width="26" height="26" rx="4" fill="var(--ink)"/><path d="M13 4a6 6 0 0 1 6 6c0 4-6 11-6 11S7 14 7 10a6 6 0 0 1 6-6z" fill="#fff"/><circle cx="13" cy="10" r="2.3" fill="var(--ink)"/></svg>
        <span>8/21-23 Birch Rd, Kelsworth 2087</span>
      </li>
      <li class="contact-line">
        <svg class="icon" viewBox="0 0 26 26" aria-label="Email"><rect width="26" height="26" rx="4" fill="var(--ink)"/><rect x="5" y="8" width="16" height="11" fill="#fff"/><path d="M5 8l8 6 8-6" fill="none" stroke="var(--ink)" stroke-width="1.5"/></svg>
        <span>info@hartiganelx.com.au</span>
      </li>
      <li class="contact-line">
        <svg class="icon" viewBox="0 0 26 26" aria-label="Website"><rect width="26" height="26" rx="4" fill="var(--ink)"/><g fill="none" stroke="#fff" stroke-width="1.5"><circle cx="13" cy="13" r="8"/><ellipse cx="13" cy="13" rx="3.5" ry="8"/><path d="M5 13h16M6.5 9h13M6.5 17h13"/></g></svg>
        <span>hartiganelx.com.au</span>
      </li>
      <li class="contact-line">
        <svg class="icon" viewBox="0 0 26 26" aria-label="ABN"><rect width="26" height="26" rx="4" fill="var(--ink)"/><path d="M10 6l-2 14M17 6l-2 14M6 10h15M5 16h15" stroke="#fff" stroke-width="2"/></svg>
        <span>ABN: 42 907 551 316</span>
      </li>
    </ul>
  </div>
</section>

<section class="card card--front" aria-label="Business card, name side">
  <svg class="card__frame" viewBox="0 0 820 469" aria-hidden="true">
    <defs>
      <linearGradient id="panelFront" x1="0" y1="0" x2="0.3" y2="1">
        <stop offset="0" stop-color="#f8f8f8"/>
        <stop offset="1" stop-color="#c6c6c6"/>
      </linearGradient>
    </defs>
    <rect x="14" y="14" width="792" height="441" fill="var(--steel-light)"/>
    <rect x="14" y="14" width="130" height="30" fill="var(--amber)"/>
    <rect x="676" y="425" width="130" height="30" fill="var(--amber)"/>
    <rect x="40" y="36" width="740" height="397" fill="var(--amber)"/>
    <rect x="60" y="56" width="700" height="357" fill="url(#panelFront)"/>
  </svg>
  <div class="card__content">
    <div class="brand">
      <div class="brand__title">
        <span class="brand__mark" aria-hidden="true"></span>
        <span class="brand__name">Hartigan Electrical</span>
      </div>
      <ul class="services" aria-label="Services">
        <li class="services__row">Licensed Electrician<span class="services__sep">•</span>Level 2 (Cat 1 &amp; 4)</li>
        <li class="services__row">Domestic<span class="services__sep">•</span>Commercial<span class="services__sep">•</span>Data</li>
        <li class="services__row">Repairs and Installations</li>
      </ul>
    </div>
  </div>
</section>

</body>
</html>
```